Postcard for Online Training Company for Real Estate Agents

We need a high-end professionally designed 2 sided color postcard to send out to Real Estate Agents to use our online, on-demand training service. We would like it to look clean and not busy. Our color scheme is Turquoise, Black and Blue. Color scheme can be seen on website address. Our main target audience are people who just entered the real estate profession. Most of them do no get an on-boarding training if they are not with a big company. We provide very low cost, highly professional training. For just $24.99 per month they have access to all the on-demand training of how to be a real estate agent. The real estate exam to get a license only has the laws and not how to be a a real estate agent.

This will also be use for small companies who do have their own training program for new real estate agent employees.

Target Market(s)

New Real Estate Agents

Industry/Entity Type

Real Estate Agent

Font styles to use
Serif
Sans Serif

Colors
33b8a4
0455a3
000000
b2b2b2

Requirements
Must have
• Both Sides Design Requirements:
• Includes Website address
• Includes Logo
• Includes Price of $24.99 per month (in some shape)
• Front needs to have these two sentences:
• “We help Real Estate agents learn how to close more business and make money”
• “On-Boarding for new agents”
• Back needs to have these 4 questions:
• "Just passed the Real Estate exam?"
• “How do I find clients?”
• “What are the steps to selling a home?”
• “How do I open escrow?”
• Website Address:
• HearthwiseSchool.com
• Logo:
• Attached
Should not have
• This should not look like it is trying to sell a house or look like it is from real estate agent

```html
<!DOCTYPE html>
<html lang="en">
<head>
<meta charset="utf-8">
<title>HearthwiseSchool Postcard</title>
<link rel="stylesheet" href="https://fonts.googleapis.com/css2?family=Crimson+Pro:wght@700&family=Fira+Sans+Extra+Condensed:wght@300;400;500&family=Fira+Sans:ital,wght@0,700;1,400&family=Montserrat:wght@800&display=swap">
<style>
  :root {
    --teal: #0aa1c0;
    --band: #999999;
    --muted: #8c8c8c;
    --paper: #ffffff;
    --page: #ffffff;
  }
  html, body {
    margin: 0;
    width: 1200px;
    height: 1200px;
    overflow: hidden;
    background: var(--page);
  }
  .postcard {
    position: absolute;
    background: var(--paper);
    box-shadow: 6px 8px 10px rgba(0,0,0,0.22);
  }
  .postcard svg { display: block; width: 100%; height: 100%; }
  .postcard--front { left: 226px; top: 44px; width: 698px; height: 542px; }
  .postcard--back  { left: 222px; top: 616px; width: 703px; height: 544px; }
  .band { fill: var(--band); }
  .flag { fill: var(--teal); }
  .wordmark {
    font-family: "Crimson Pro", Georgia, serif;
    font-weight: 700;
    fill: var(--teal);
  }
  .url {
    font-family: "Fira Sans Extra Condensed", "Arial Narrow", sans-serif;
    font-weight: 300;
    fill: var(--muted);
  }
  .price {
    font-family: "Fira Sans Extra Condensed", "Arial Narrow", sans-serif;
    font-weight: 500;
    fill: #fff;
  }
  .price__amount { font-family: "Fira Sans", Arial, sans-serif; font-weight: 700; }
  .tagline {
    font-family: "Fira Sans", Arial, sans-serif;
    font-style: italic;
    font-variant: small-caps;
    fill: #fff;
  }
  .headline {
    font-family: "Montserrat", Arial, sans-serif;
    font-weight: 800;
    font-variant: small-caps;
    letter-spacing: 0.5px;
    fill: #fff;
  }
  .question {
    font-family: "Fira Sans Extra Condensed", "Arial Narrow", sans-serif;
    font-weight: 300;
    fill: #fff;
  }
</style>
</head>
<body>

<section class="postcard postcard--front" aria-label="Postcard front">
  <svg viewBox="0 0 873 677" preserveAspectRatio="none">
    <polygon class="band" points="0,413 308,315 873,230 873,677 0,677"/>
    <polygon class="flag" points="0,245 363,328 0,413"/>
    <text class="wordmark" x="436" y="217" font-size="64" text-anchor="middle">HearthwiseSchool</text>
    <text class="url" x="430" y="253" font-size="24" text-anchor="middle">HearthwiseSchool.com</text>
    <text class="price" x="32" y="340" font-size="30"><tspan class="price__amount">$24.99</tspan> per month</text>
    <text class="tagline" x="437" y="480" font-size="23" text-anchor="middle">We help Real Estate agents learn how to close more business and make money</text>
    <text class="headline" x="437" y="512" font-size="24" text-anchor="middle">On-Boarding for new agents</text>
  </svg>
</section>

<section class="postcard postcard--back" aria-label="Postcard back">
  <svg viewBox="0 0 879 680" preserveAspectRatio="none">
    <polygon class="band" points="0,198 159,235 456,278 429,546 0,567"/>
    <polygon class="flag" points="159,235 413,172 437,290"/>
    <text class="wordmark" x="36" y="120" font-size="54">HearthwiseSchool</text>
    <text class="price" x="242" y="238" font-size="25"><tspan class="price__amount">$24.99</tspan> per month</text>
    <text class="question" x="23" y="327" font-size="30">Just passed the Real Estate exam?</text>
    <text class="question" x="23" y="369" font-size="30">How do I find clients?</text>
    <text class="question" x="23" y="411" font-size="30">What are the steps to selling a home?</text>
    <text class="question" x="23" y="453" font-size="30">How do I open escrow?</text>
    <text class="url" x="589" y="397" font-size="25">HearthwiseSchool.com</text>
  </svg>
</section>

</body>
</html>
```